Harbor Sushi & Steak Dinner Menu

I'm looking for a MENU design with a particular feel. I want to have a base template made that I can then use for future alterations to the menu; ie I can go in and change out different entrees as the menu changes but the template will remain the same. (Ideally it would be in an Apple Pages format.). Also ideally - dinner menu will occupy 2 pages 8.5 x 11. The restaurant's name is Harbor. It is a MODERN steak house that will also feature Sushi, a Raw Bar, Exquisite Cocktails and a sophisticated nightlife crowd. I have attached our LOGO, a secondary logo that we will be featuring throughout the project including on the menu cover (the gold U). Finally - I have attached the content that we would like to see. AGAIN - I REITERATE: High end dining and lounge atmosphere. A couple of restaurants / menus that I love are Morvendel in NYC and Pellucid Steakhouse in Long Island NY. Please do not duplicate - just trying to offer some suggestions.

Requirements
Must have
• A sophisticated and elegant feel without being stuffy or old.

```html
<!DOCTYPE html>
<html lang="en">
<head>
<meta charset="utf-8">
<title>Harbor Sushi &amp; Steak — Dinner Menu</title>
<link href="https://fonts.googleapis.com/css2?family=Titillium+Web:wght@600;700&family=Mulish:wght@400;600;800&family=Libre+Baskerville:wght@700&display=swap" rel="stylesheet">
<style>
  :root{
    --gold:#c6a46a;
    --gold-soft:#d9c29a;
    --ink:#161616;
    --red:#c3261c;
    --paper:#ffffff;
  }
  *{box-sizing:border-box;margin:0;padding:0}
  html,body{width:880px;height:1200px;overflow:hidden;background:var(--paper)}
  .menu{position:relative;width:880px;height:1200px;font-family:"Mulish",sans-serif;color:var(--ink)}

  /* frame */
  .rule{position:absolute;background:var(--gold)}
  .rule-h{height:2px}
  .rule-v{width:2px}
  .frame-dot{position:absolute;width:14px;height:14px;border-radius:50%;background:var(--gold)}
  .ornament{position:absolute;background:var(--gold-soft);opacity:.75}
  .ornament-corner{width:66px;height:66px;border-radius:4px}
  .ornament-crest{width:160px;height:42px;border-radius:21px}

  /* brand */
  .brand{position:absolute;left:340px;top:76px;width:200px;text-align:center}
  .brand-name{font-family:"Titillium Web",sans-serif;font-weight:700;font-size:40px;letter-spacing:6px;color:var(--gold);line-height:1}

  /* section titles */
  .section-title{position:absolute;font-family:"Titillium Web",sans-serif;font-weight:700;font-size:23px;letter-spacing:.5px;color:var(--gold);padding:0 2px 1px;border-bottom:1px solid var(--gold-soft);line-height:1.2}

  /* items */
  .item{position:absolute}
  .col-left{left:70px;width:346px}
  .col-right{left:472px;width:342px}
  .item-head{display:flex;align-items:flex-end}
  .item-name{font-weight:800;font-size:13px;letter-spacing:.3px;white-space:nowrap;line-height:1.2}
  .item-name .note{font-weight:400;letter-spacing:0}
  .leader{flex:1;border-bottom:1px dotted #555;margin:0 4px 4px 10px;min-width:20px}
  .price{font-family:"Libre Baskerville",serif;font-weight:700;font-size:19px;color:var(--gold);line-height:1}
  .item-desc{font-size:12px;line-height:1.15;margin-top:2px}
  .item-lg .item-name{font-size:15px}
  .item-lg .item-desc{font-size:14.5px;line-height:1.05}

  .raw-list{position:absolute;left:474px;top:804px;list-style:none}
  .raw-list li{font-weight:800;font-size:13px;letter-spacing:.3px;height:23.5px}
  .accent{position:absolute;left:472px;font-weight:800;font-size:13px;color:var(--red);letter-spacing:.3px}
  .plain{position:absolute;left:472px;font-size:12px;line-height:1.15}
  .bold-list{position:absolute;left:474px;font-weight:800;font-size:13px;line-height:1.3;letter-spacing:.3px}
</style>
</head>
<body>
<main class="menu">
  <!-- frame lines -->
  <div class="rule rule-h" style="left:140px;top:37px;width:140px"></div>
  <div class="rule rule-h" style="left:600px;top:37px;width:140px"></div>
  <div class="rule rule-h" style="left:140px;top:1157px;width:140px"></div>
  <div class="rule rule-h" style="left:600px;top:1157px;width:140px"></div>
  <div class="rule rule-v" style="left:40px;top:110px;height:450px"></div>
  <div class="rule rule-v" style="left:40px;top:630px;height:460px"></div>
  <div class="rule rule-v" style="left:838px;top:110px;height:450px"></div>
  <div class="rule rule-v" style="left:838px;top:630px;height:460px"></div>
  <div class="rule rule-v" style="left:440px;top:188px;height:922px"></div>
  <div class="frame-dot" style="left:34px;top:586px"></div>
  <div class="frame-dot" style="left:832px;top:586px"></div>

  <div class="ornament ornament-corner" role="img" aria-label="Gold fleur-de-lis corner ornament" style="left:42px;top:36px"></div>
  <div class="ornament ornament-corner" role="img" aria-label="Gold fleur-de-lis corner ornament" style="left:772px;top:36px"></div>
  <div class="ornament ornament-corner" role="img" aria-label="Gold fleur-de-lis corner ornament" style="left:42px;top:1096px"></div>
  <div class="ornament ornament-corner" role="img" aria-label="Gold fleur-de-lis corner ornament" style="left:772px;top:1096px"></div>
  <div class="ornament ornament-crest" role="img" aria-label="Gold scroll flourish" style="left:360px;top:10px"></div>
  <div class="ornament ornament-crest" role="img" aria-label="Gold scroll flourish" style="left:360px;top:1138px"></div>

  <header class="brand"><div class="brand-name">HARBOR</div></header>

  <!-- left column -->
  <h2 class="section-title" style="left:114px;top:152px">SUSHI / SASHIMI</h2>
  <div class="item col-left" style="top:194px"><div class="item-head"><span class="item-name">TORO <span class="note">blue fin tuna belly (gf)</span></span><span class="leader"></span><span class="price">$0.00</span></div></div>
  <div class="item col-left" style="top:221px"><div class="item-head"><span class="item-name">EBI <span class="note">cooked shrimp (gf)</span></span><span class="leader"></span><span class="price">$0.00</span></div></div>
  <div class="item col-left" style="top:248px"><div class="item-head"><span class="item-name">HAMACHI <span class="note">yellowtail (gf)</span></span><span class="leader"></span><span class="price">$0.00</span></div></div>
  <div class="item col-left" style="top:274px"><div class="item-head"><span class="item-name">UNI <span class="note">sea urchin (gf)</span></span><span class="leader"></span><span class="price">$0.00</span></div></div>
  <div class="item col-left" style="top:300px"><div class="item-head"><span class="item-name">HIRAME <span class="note">fluke (gf)</span></span><span class="leader"></span><span class="price">$0.00</span></div></div>
  <div class="item col-left" style="top:330px"><div class="item-head"><span class="item-name">UNAGI <span class="note">fresh water eel (gf)</span></span><span class="leader"></span><span class="price">$0.00</span></div></div>
  <div class="item col-left" style="top:357px"><div class="item-head"><span class="item-name">SAKE <span class="note">salmon (gf)</span></span><span class="leader"></span><span class="price">$0.00</span></div></div>
  <div class="item col-left" style="top:387px"><div class="item-head"><span class="item-name">MADAI <span class="note">red snapper (gf)</span></span><span class="leader"></span><span class="price">$0.00</span></div></div>
  <div class="item col-left" style="top:414px"><div class="item-head"><span class="item-name">MAGURO <span class="note">tuna (gf)</span></span><span class="leader"></span><span class="price">$0.00</span></div></div>

  <h2 class="section-title" style="left:114px;top:456px">SUSHI PLATTERS</h2>
  <div class="item col-left" style="top:498px"><div class="item-head"><span class="item-name">SMALL</span><span class="leader"></span><span class="price">$0.00</span></div><p class="item-desc">Five Pieces assorted sushi, nine pieces sashimi,<br>spicy tuna roll (gf)</p></div>
  <div class="item col-left" style="top:562px"><div class="item-head"><span class="item-name">LARGE</span><span class="leader"></span><span class="price">$0.00</span></div><p class="item-desc">Eight Pieces assorted sushi, eighteen pieces<br>of sashimi, alaskan roll, rainbow roll (gf)</p></div>

  <h2 class="section-title" style="left:110px;top:639px">CLASSIC ROLLS</h2>
  <div class="item col-left" style="top:687px"><div class="item-head"><span class="item-name">YELLOWTAIL</span><span class="leader"></span><span class="price">$0.00</span></div><p class="item-desc">inside out roll with scallions (gf)</p></div>
  <div class="item col-left" style="top:736px"><div class="item-head"><span class="item-name">SPICY TUNA OR SALMON OR<br>YELLOWTAIL</span><span class="leader"></span><span class="price">$0.00</span></div><p class="item-desc">spicy mayo</p></div>
  <div class="item col-left" style="top:802px"><div class="item-head"><span class="item-name">CALIFORNIA</span><span class="leader"></span><span class="price">$0.00</span></div><p class="item-desc">crab meat, cucumber and avocado (gf)</p></div>
  <div class="item col-left item-lg" style="top:850px"><div class="item-head"><span class="item-name">VEGETABLE</span><span class="leader"></span><span class="price">$0.00</span></div><p class="item-desc">avocado, cucumber,<br>asparagus and pickled reddish (gf)</p></div>
  <div class="item col-left item-lg" style="top:920px"><div class="item-head"><span class="item-name">SPIDER</span><span class="leader"></span><span class="price">$0.00</span></div><p class="item-desc">soft shell crab<br>and avocado with eel sauce</p></div>
  <div class="item col-left item-lg" style="top:990px"><div class="item-head"><span class="item-name">SHRIMP TEMPURA</span><span class="leader"></span><span class="price">$0.00</span></div><p class="item-desc">deep fried tempura shrimp<br>and eel sauce</p></div>
  <div class="item col-left item-lg" style="top:1055px"><div class="item-head"><span class="item-name">ALASKAN</span><span class="leader"></span><span class="price">$0.00</span></div><p class="item-desc">salmon and avocado (gf)</p></div>

  <!-- right column -->
  <h2 class="section-title" style="left:534px;top:153px">SPECIAL ROLLS</h2>
  <div class="item col-right" style="top:194px"><div class="item-head"><span class="item-name">THE HARBOR</span><span class="leader"></span><span class="price">$0.00</span></div><p class="item-desc">tuna, salmon, yellowtail, avocado,<br>spicy mayo, soy bean paper</p></div>
  <div class="item col-right" style="top:256px"><div class="item-head"><span class="item-name">KING CRAB RAINBOW</span><span class="leader"></span><span class="price">$0.00</span></div><p class="item-desc">king crab, avocado, cucumbers,<br>assorted fish on top</p></div>
  <div class="item col-right" style="top:321px"><div class="item-head"><span class="item-name">EMPRESS</span><span class="leader"></span><span class="price">$0.00</span></div><p class="item-desc">Shrimp tempura, spicy tuna on top,<br>eel sauce, spicy mayo</p></div>
  <div class="item col-right" style="top:388px"><div class="item-head"><span class="item-name">SPICY GIRL</span><span class="leader"></span><span class="price">$0.00</span></div><p class="item-desc">Spicy crunchy crab meat, cucumber,<br>shrimp on top</p></div>
  <div class="item col-right" style="top:456px"><div class="item-head"><span class="item-name">DRAGON</span><span class="leader"></span><span class="price">$0.00</span></div><p class="item-desc">Eel, cucumber, avocado,<br>and tobiko on top, eel sauce</p></div>
  <div class="item col-right" style="top:525px"><div class="item-head"><span class="item-name">YUMMY</span><span class="leader"></span><span class="price">$0.00</span></div><p class="item-desc">spicy crunchy salmon, avocado,<br>mango and salmon on top</p></div>
  <div class="item col-right" style="top:595px"><div class="item-head"><span class="item-name">NO. 9</span><span class="leader"></span><span class="price">$0.00</span></div><p class="item-desc">Shrimp Tempura, avocado,<br>kani, spicy mayo, tobiko</p></div>
  <div class="item col-right" style="top:669px"><div class="item-head"><span class="item-name">SUNRISE ROLL</span><span class="leader"></span><span class="price">$0.00</span></div><p class="item-desc">spicy crunchy tuna and avocado,<br>spicy crunchy salmon on top</p></div>

  <h2 class="section-title" style="left:528px;top:756px">SEAFOOD RAW BAR</h2>
  <ul class="raw-list">
    <li>LOBSTER COCKTAIL</li>
    <li>SHRIMP COCKTAIL</li>
    <li>CLAMS ON THE HALF SHELL</li>
    <li>OYSTERS ON THE HALF SHELL</li>
    <li>COLOSSAL CRAB COCKTAIL</li>
  </ul>
  <p class="accent" style="top:932px">RAW BAR PLATE FOR ONE:</p>
  <p class="plain" style="top:950px">Two Shrimp, Half of a One Pound Lobster, Two Clams,<br>One East Coast Oyster, One West Coast Oyster</p>

  <h2 class="section-title" style="left:528px;top:1009px">SEAFOOD PLATTERS (GF)</h2>
  <p class="bold-list" style="top:1056px">SHRIMP, OYSTERS, CLAMS,<br>LOBSTER AND CRAB</p>
  <p class="accent" style="top:1102px">LARGE OR COLOSSAL</p>
</main>
</body>
</html>
```